Make a flyer for a love,sex,relationship panel

Im lookinf for somebody that can make me a flyer within the next two days for a love,sex,relationship panel that i am having at my college

time is 8:00pm
place is the Hearth
the school is thornbury college
The organization that is putting this on is HCL(Harmony Campus League)

students only

Any and all question can be asked

The Point of the panel is that it gives students a chance to freely asking anything that want about love,sex,or relationship because as college students is something that most of us go through

we cant it to be fun at the the same time helpful to somebody

Also put some type of picture on there

also put like example questions that can be asked

anything else that you would like to know just ask

```html
<!DOCTYPE html>
<html lang="en">
<head>
<meta charset="utf-8">
<title>Love, Sex &amp; Relationship Panel — Harmony Campus League</title>
<link href="https://fonts.googleapis.com/css2?family=League+Spartan:wght@600;700;800&family=Oswald:wght@300&family=Pathway+Gothic+One&family=Libre+Baskerville&display=swap" rel="stylesheet">
<style>
  :root {
    --paper: #e3e3e3;
    --teal: #45a5ae;
    --teal-soft: #7fbfc5;
    --ink: #2b2b2b;
    --rule: #8a8a8a;
  }
  * { margin: 0; padding: 0; box-sizing: border-box; }
  html, body { width: 900px; height: 1200px; overflow: hidden; background: var(--paper); }
  .flyer {
    position: relative;
    width: 900px;
    height: 1200px;
    background: var(--paper);
    color: var(--ink);
    overflow: hidden;
  }
  .hands-art {
    position: absolute;
    left: 0; top: 0;
    width: 900px; height: 1060px;
  }
  .organiser {
    position: absolute;
    left: 0; right: 0; top: 14px;
    text-align: center;
    font-family: "League Spartan", sans-serif;
    font-weight: 700;
    font-size: 38px;
    line-height: 50px;
    letter-spacing: 2px;
  }
  .article {
    position: absolute;
    left: 412px; top: 128px;
    font-family: "League Spartan", sans-serif;
    font-weight: 700;
    font-size: 38px;
  }
  .title {
    position: absolute;
    left: 246px; top: 180px;
    font-family: "League Spartan", sans-serif;
    font-weight: 700;
    line-height: 1;
  }
  .title-love {
    display: flex; align-items: flex-end;
    font-size: 130px; height: 108px; letter-spacing: 2px;
  }
  .title-love .heart { width: 92px; height: 86px; margin: 0 4px 12px 2px; }
  .title-sex { font-size: 104px; margin-top: 14px; letter-spacing: 1px; }
  .title-sex .amp {
    font-family: "Libre Baskerville", serif;
    font-weight: 400;
    font-size: 76px;
    margin-left: 16px;
  }
  .title-relationship { font-size: 74px; margin-top: 4px; letter-spacing: 0; }
  .title-panel { font-size: 40px; margin-top: -6px; letter-spacing: 2px; }
  .sample-questions {
    position: absolute;
    left: 0; right: 0; top: 588px;
    text-align: center;
    font-family: "League Spartan", sans-serif;
    font-weight: 700;
    font-size: 37px;
    line-height: 56px;
    letter-spacing: 2.5px;
  }
  .invite {
    position: absolute;
    left: 0; right: 0; top: 752px;
    text-align: center;
    font-family: "Oswald", sans-serif;
    font-weight: 300;
    font-size: 64px;
    line-height: 85px;
    letter-spacing: 0.5px;
  }
  .footer-rule {
    position: absolute;
    left: 0; right: 0; top: 1138px;
    border-top: 2px solid var(--rule);
  }
  .details {
    position: absolute;
    left: 0; right: 0; top: 1152px;
    text-align: center;
    font-family: "Pathway Gothic One", sans-serif;
    font-size: 32px;
    letter-spacing: 2px;
  }
</style>
</head>
<body>
<main class="flyer">
  <svg class="hands-art" viewBox="0 0 900 1060" role="img" aria-label="Silhouette illustration of two arms reaching in and holding hands">
    <defs>
      <radialGradient id="handsGlow" cx="0.5" cy="0.55" r="0.6">
        <stop offset="0" stop-color="var(--teal)"/>
        <stop offset="0.7" stop-color="var(--teal-soft)"/>
        <stop offset="1" stop-color="var(--paper)"/>
      </radialGradient>
    </defs>
    <rect x="0" y="0" width="900" height="1060" fill="url(#handsGlow)"/>
  </svg>

  <header class="organiser">HARMONY CAMPUS LEAGUE<br>ORGANISE</header>
  <div class="article">A</div>

  <h1 class="title">
    <div class="title-love">L<svg class="heart" viewBox="0 0 100 92" aria-hidden="true"><path d="M50 92 L8 48 C-6 32 0 4 26 2 C38 1 46 8 50 16 C54 8 62 1 74 2 C100 4 106 32 92 48 Z" fill="var(--ink)"/></svg>VE</div>
    <div class="title-sex">SEX<span class="amp">&amp;</span></div>
    <div class="title-relationship">RELATIONSHIP</div>
    <div class="title-panel">PANEL</div>
  </h1>

  <p class="sample-questions">WHY AM I JEALOUS?AM I NORMAL?<br>AM I GOOD ENOUGH? WHEN IS TIME?</p>

  <p class="invite">YOU HAVE OTHER QUESTIONS?<br>WE ALL DO, SO COME AND<br>JOIN US AT THE HEARTH AT 8:00 PM<br>AND ASK ANYTHING YOU WANT!</p>

  <div class="footer-rule"></div>
  <footer class="details">8:PM AT THE HEARTH - STUDENTS ONLY; THORNBURY COLLEGE</footer>
</main>
</body>
</html>
```